Ticket Website Design

The project is to design a website for a ticket business. We sell ticket for sports, theater and concerts.

- Below are some ticket design styles that we like -

PassHarbor.com
BrightRowz.com
GateNook.com
AdmitPlacing.com
Plov.com
FlenTrek.com

- Homepage features -

The main navigation should be the following links:
Upcoming, Sports, Concerts, Theater, Las Vegas, Location, Other

The main navigation should have a drop down menu designed.

The homepage should have a featured search box that is in a location that can be carried through to an internal page.

The site should be around 1000px width

We don't have a logo yet so you can use a placeholder in the logo location. I'll work to upload a placeholder logo if a designer don't have one.

We’d like to keep the background of the site lighter and not a dark solid background

You are free to do colors to your liking. However, please make them good combination colors and nothing that is very bright (i.e. Lime green). Some possible example colors would be “black/red”, “blue/orange”

We'd like the logo in the top left of the site.

- Other homepage elements -

Featured Events (Slider Box with Image)
Events In the Next 60 Days (Listing)
Newsletter (Form)
Buyer Guarantee (Design Box)
Testimonials (2 Featured Testimonials)
Featured Sports Tickets (Heading/Listing)
Featured Concert Tickets (Heading/Listing)
Featured Theater Tickets (Heading/Listing)
Featured Tickets By City (Heading/Listing)
Featured Phone Number / Less Featured International Number
Social Icons
“Your Location” See PassHarbor.com in the header. This shows the location of the visitor and features events in their area. They can click a small button to edit that location.

- What we are looking for overall -

We are looking for a high quality professional homepage design that contains all of the homepage features listed. While you are designing the homepage, please keep in mind the transition to an internal page. We want it to be a smooth transition. For example: if there is a column on the homepage, that column follows through on the internal page.

If you have some thoughts or questions on that let me know and I’d be happy to answer before you design.
Updates

Project Deadline Extended
Reason: A few designers asked for a few more days to submit their designs. Thanks for understanding. Let me know if anyone has any questions. Thanks, Dorn

Target Market(s)

18-35

Industry/Entity Type

Events

Requirements
Should not have
• No really bright colors (lime green/pink, etc.)

```html
<!DOCTYPE html>
<html lang="en">
<head>
<meta charset="utf-8">
<title>Your Company – Tickets</title>
<link href="https://fonts.googleapis.com/css2?family=Oswald:wght@300;400&display=swap" rel="stylesheet">
<style>
:root{
  --maroon:#7a0b0b;
  --maroon-dark:#5e0000;
  --brand:#8e1c1c;
  --ink:#111;
  --paper:#fff;
  --grey:#cfcfcf;
  --gold:#f7c20a;
}
*{box-sizing:border-box;margin:0;padding:0}
html,body{width:1176px;height:1200px;overflow:hidden;background:var(--paper)}
body{position:relative;font-family:'Oswald',sans-serif;font-weight:300;color:var(--ink);letter-spacing:-.3px}
.abs{position:absolute}
.navbar{left:0;width:1176px;height:54px;background:var(--maroon);box-shadow:0 6px 8px rgba(0,0,0,.35)}
.navbar.top{top:82px}
.navbar.bottom{top:1070px}
.nav-links{position:absolute;left:269px;top:0;height:54px;display:flex;align-items:center;gap:24px;list-style:none}
.nav-links li{color:#fff;font-size:21px}
.logo-art{left:58px;top:14px;width:140px;height:140px;background:linear-gradient(135deg,#f7a45e,#ef7f3a);border-radius:8px;transform:rotate(-8deg);z-index:2}
.brand{left:188px;top:26px;font-size:39px;font-weight:400;color:var(--brand);z-index:3}
.contact{left:919px;top:46px;font-size:20px;font-weight:300}
.search{left:923px;top:90px;width:193px;height:38px;background:#fff;border-radius:19px;box-shadow:inset 0 0 4px #888;display:flex;align-items:center;padding-left:18px;font-size:15px;font-style:italic;color:#888}
.search svg{position:absolute;right:14px;top:6px}
.dropdown{left:582px;top:137px;width:193px;height:226px;background:var(--grey);border-radius:16px;box-shadow:0 2px 6px rgba(0,0,0,.4);padding:2px 0 0 18px;list-style:none;z-index:4}
.dropdown li{font-size:20px;line-height:29px}
.sidebar-frame{left:16px;top:160px;width:222px;height:688px;background:var(--maroon)}
.sidebar-inner{left:22px;top:166px;width:209px;height:670px;border:2px solid var(--maroon);background:linear-gradient(#fff 25%,#a73b3b 100%);padding:10px 0 0 6px;white-space:nowrap}
.sidebar-inner .near{font-weight:300;font-size:19px;letter-spacing:-.6px}
.sidebar-inner .place{font-weight:400;font-size:20px;margin-top:8px}
.set-loc{display:block;margin:2px 0 0 4px;width:188px;height:42px;background:var(--maroon);color:#fff;font-size:19px;line-height:42px;text-align:center;box-shadow:0 3px 5px rgba(0,0,0,.4)}
.artist-list{list-style:none;margin-top:28px;padding-left:6px}
.artist-list li{font-size:20px;line-height:28.8px}
.banner{left:258px;top:166px;width:869px;height:194px;background:linear-gradient(#fff 0%,#777 45%,#000 70%);box-shadow:3px 3px 6px rgba(0,0,0,.4)}
.newsletter{left:260px;top:380px;width:852px;height:126px;background:var(--maroon-dark);border-radius:24px;box-shadow:0 4px 6px rgba(0,0,0,.4)}
.newsletter h2{position:absolute;left:68px;top:16px;font-size:25px;font-weight:400;color:#fff;letter-spacing:-.5px}
.email{position:absolute;left:76px;top:61px;width:591px;height:49px;background:#fff;border-radius:14px;padding-left:36px;line-height:49px;font-size:20px;font-style:italic;color:#999}
.guarantee{left:1012px;top:386px;width:116px;height:116px;border-radius:50%;background:radial-gradient(#f9a81a 55%,var(--gold) 56%)}
.card{width:383px;height:175px;border:2px solid var(--maroon);background:#fff}
.tab{width:200px;height:56px;background:var(--maroon);color:#fff;font-size:20px;font-weight:400;text-align:center;line-height:28px;box-shadow:2px 3px 5px rgba(0,0,0,.4)}
.card-art{position:absolute}
.card ul{position:absolute;left:230px;top:20px;list-style:none;white-space:nowrap}
.card li{font-size:20px;line-height:29px}
.social{top:1034px;width:55px;height:55px;border-radius:8px;background:var(--maroon-dark);color:#fff;font-size:13px;font-weight:400;display:flex;align-items:center;justify-content:center;box-shadow:0 2px 4px rgba(0,0,0,.4)}
</style>
</head>
<body>

<header>
  <div class="abs logo-art" role="img" aria-label="Orange admit-one ticket stubs"></div>
  <div class="abs brand">Your Company</div>
  <div class="abs contact">Contact Us 1-800-555-0142</div>
  <nav class="abs navbar top">
    <ul class="nav-links">
      <li>Upcoming</li><li>Sports</li><li>Concerts</li><li>Theater</li><li>Las Vegas</li><li>By Location</li><li>Other Events</li>
    </ul>
  </nav>
  <div class="abs search">Search For Tickets
    <svg width="26" height="28" viewBox="0 0 26 28"><circle cx="14" cy="11" r="9" fill="none" stroke="#111" stroke-width="2"/><line x1="8" y1="18" x2="3" y2="26" stroke="#111" stroke-width="2"/></svg>
  </div>
</header>

<aside>
  <div class="abs sidebar-frame"></div>
  <div class="abs sidebar-inner">
    <div class="near">Events Happening Near You</div>
    <div class="place">Ocean New Jersey</div>
    <span class="set-loc">Set Your Location</span>
    <ul class="artist-list">
      <li>Marisol Vey tickets</li><li>Dario Lune tickets</li><li>Kestrel Drive Tour tickets</li><li>Jory Castel tickets</li><li>Jalen Thorne tickets</li><li>Luke Harlan tickets</li><li>Five Harbor tickets</li><li>Roux tickets</li><li>Tessa Rowe tickets</li><li>The Falconers ticket</li>
    </ul>
  </div>
</aside>

<div class="abs banner" role="img" aria-label="Silhouetted concert crowd with raised hands"></div>
<ul class="abs dropdown">
  <li>Tours</li><li>Concerts</li><li>Events</li><li>Dinner theatre</li><li>Drop Down Menu</li>
</ul>

<section class="abs newsletter">
  <h2>Get Real Saving Delivered Right To Your&nbsp; Inbox Join Our Mailing List</h2>
  <div class="email">Enter Your Email Address&nbsp; Here</div>
</section>
<div class="abs guarantee" role="img" aria-label="Money back guarantee seal"></div>

<section class="abs card" style="left:255px;top:563px">
  <div class="card-art" style="left:4px;top:44px;width:152px;height:127px;background:linear-gradient(#3a1b0e,#222 55%,#ddd)" role="img" aria-label="American football and soccer ball"></div>
  <ul><li>New York Harbormen</li><li>Boston Bay Hawks</li><li>Continental Gold Cup</li><li>Continental Soccer</li><li>Pro All Star Game</li></ul>
</section>
<div class="abs tab" style="left:255px;top:541px">Featured Sports<br>Tickets</div>

<section class="abs card" style="left:749px;top:563px">
  <div class="card-art" style="left:50px;top:46px;width:130px;height:125px;background:linear-gradient(90deg,#fff,#111 40%,#111 60%,#fff)" role="img" aria-label="Silhouette of a singer with microphone"></div>
  <ul><li>The Falconers</li><li>Luke Harlan</li><li>Gulf Coast Line</li><li>Country Fest Pass</li><li>Whitman Square</li></ul>
</section>
<div class="abs tab" style="left:749px;top:541px">Featured Concert<br>Tickets</div>

<section class="abs card" style="left:257px;top:771px">
  <div class="card-art" style="left:0;top:40px;width:232px;height:133px;background:linear-gradient(#fff 10%,#222 45%,#222)" role="img" aria-label="City skyline silhouette"></div>
  <ul><li>New York</li><li>Washington</li><li>Las Vegas</li><li>Las Angels</li><li>Houston</li></ul>
</section>
<div class="abs tab" style="left:257px;top:747px">Featured Tickets By<br>City</div>

<section class="abs card" style="left:749px;top:771px">
  <div class="card-art" style="left:6px;top:50px;width:200px;height:115px;background:radial-gradient(#111 45%,#fff 75%)" role="img" aria-label="Comedy and tragedy theatre masks"></div>
  <ul><li>The Book Of Marlow</li><li>Gilded</li><li>Velvet Heels</li><li>The Desert King</li><li>Nola - The Musical</li></ul>
</section>
<div class="abs tab" style="left:749px;top:752px">Featured Theatre<br>Tickets</div>

<footer>
  <nav class="abs navbar bottom">
    <ul class="nav-links">
      <li>Upcoming</li><li>Sports</li><li>Concerts</li><li>Theater</li><li>Las Vegas</li><li>By Location</li><li>Other Events</li>
    </ul>
  </nav>
  <div class="abs social" style="left:885px">Chirp</div>
  <div class="abs social" style="left:954px">Pinly</div>
  <div class="abs social" style="left:1022px">Facely</div>
  <div class="abs social" style="left:1091px">Linkora</div>
</footer>

</body>
</html>
```